Cat-products company needs smart, yet endearing, business card

We need a business card design for a new, but up-and-running, business based in Honolulu, Hawaii. The business is Purrlane Nest Co. Our first product is the most environmentally-friendly cat grass kit ever seen on the planet. Future products, currently in the R&D phase, will include a variety of exciting cat scratchers. We also do consulting work to help apartment-dwellers make their home more cat-friendly and, in the future, plan on doing full, custom installs of structure to create high walkways for cats.

Target Market(s)

Middle-aged, apartment-dwelling, middle-class workers who own 1 or more cats and who dote on them.

Industry/Entity Type

Pet Care

Contact Information for Business Card

A striking, professional, yet warm and friendly design is what we're after.

Font styles to use
Serif
Sans Serif
Other font styles liked:
• Comfortaa

Colors

Designer to choose colors to be used in the design.

Requirements
Must have
• The company logo: (see attachment)
• The company name: Purrlane Nest Co
• The web address: www.purrlanenestco.example
• Email: support@purrlanenestco.example
• Phone: +1 (808) 555 0172
• Update (Fri Jun 30 3017 7:45pm Hawaii Time) I would like, is possible, uploaded picture of the cat grass kit on the back of the card with some text along the lines of: Purrlane Nest Co - Where The Freshest Kitty Sprouts Begin
Nice to have
• A cat picture, cartoon, real or silhouette that illustrates cats in action and/or relaxing; ie using the apartment space to live, play and relax in and being well-contented.
• Most of the website is done in the font: Comfortaa. It might be nice to continue using this for brand consistency.
Should not have
• Hard-to-read fonts.

```html
<!DOCTYPE html>
<html lang="en">
<head>
<meta charset="utf-8">
<title>Purrlane Nest Co – Business Card</title>
<link rel="stylesheet" href="https://fonts.googleapis.com/css2?family=Fredoka:wght@600&family=Oswald:wght@400;600&family=Roboto:wght@400&display=swap">
<style>
  :root {
    --page: #e4e4e4;
    --card: #ffffff;
    --brown: #5a3530;
    --gold: #f7b30a;
    --ink: #3d3d3d;
    --muted: #5c5c5c;
    --rule: #b9b9b9;
    --grass-dark: #3f7a1e;
    --grass: #6ab330;
    --fur: #e08a3c;
    --fur-light: #f3e6da;
  }
  * { box-sizing: border-box; margin: 0; padding: 0; }
  html, body { width: 1200px; height: 1200px; overflow: hidden; }
  body {
    background: var(--page);
    display: flex;
    flex-direction: column;
    align-items: center;
    justify-content: center;
    gap: 60px;
  }
  .card {
    position: relative;
    width: 900px;
    height: 514px;
    overflow: hidden;
    box-shadow: 0 10px 28px rgba(0,0,0,.16);
  }

  /* Front */
  .card--front { background: var(--card); }
  .front__band {
    position: absolute; left: 0; right: 0; bottom: 0;
    height: 64px; background: var(--brown);
  }
  .front__accent {
    position: absolute; left: 0; right: 0; bottom: 76px;
    height: 6px; background: var(--gold);
  }
  .brand {
    position: absolute; left: 64px; top: 150px;
    display: flex; align-items: center; gap: 18px;
  }
  .brand__mark { width: 40px; height: 40px; background: var(--gold); }
  .brand__name {
    font-family: "Fredoka", sans-serif; font-weight: 600;
    font-size: 40px; line-height: 1.0; color: var(--brown);
  }
  .divider {
    position: absolute; left: 400px; width: 1px; background: var(--rule);
  }
  .divider--top { top: 112px; height: 88px; }
  .divider--bottom { top: 236px; height: 120px; }
  .person { position: absolute; left: 430px; top: 116px; }
  .person__name {
    font-family: "Oswald", sans-serif; font-size: 42px; line-height: 1;
    letter-spacing: .5px; text-transform: uppercase;
  }
  .person__first { color: var(--gold); font-weight: 400; }
  .person__last { color: var(--brown); font-weight: 600; }
  .person__role {
    font-family: "Roboto", sans-serif; font-size: 22px; color: var(--muted);
    margin-top: 8px;
  }
  .contacts {
    position: absolute; left: 430px; top: 244px;
    list-style: none; font-family: "Roboto", sans-serif;
    font-size: 23px; color: var(--ink);
  }
  .contacts li { display: flex; align-items: center; gap: 14px; height: 38px; }
  .contacts svg { width: 22px; height: 22px; fill: var(--brown); flex: none; }

  /* Back */
  .card--back { background: var(--grass-dark); }
  .back__photo {
    position: absolute; inset: 0;
    background:
      radial-gradient(ellipse 34% 48% at 52% 48%, var(--fur-light) 0%, rgba(243,230,218,.0) 100%),
      radial-gradient(ellipse 40% 60% at 66% 78%, var(--fur) 0%, rgba(224,138,60,0) 100%),
      linear-gradient(135deg, var(--grass) 0%, var(--grass-dark) 100%);
  }
  .back__brand {
    position: absolute; right: 96px; bottom: 70px;
    font-family: "Fredoka", sans-serif; font-weight: 600;
    font-size: 54px; line-height: 1; color: var(--brown);
  }
</style>
</head>
<body>

  <section class="card card--front" aria-label="Business card front">
    <div class="brand">
      <span class="brand__mark" aria-hidden="true"></span>
      <span class="brand__name">Purrlane<br>Nest Co</span>
    </div>

    <span class="divider divider--top" aria-hidden="true"></span>
    <span class="divider divider--bottom" aria-hidden="true"></span>

    <div class="person">
      <p class="person__name"><span class="person__first">Kai</span> <span class="person__last">Malana</span></p>
      <p class="person__role">Director</p>
    </div>

    <ul class="contacts">
      <li>
        <svg viewBox="0 0 24 24" aria-hidden="true"><path d="M6.6 10.8a15.2 15.2 0 0 0 6.6 6.6l2.2-2.2c.3-.3.7-.4 1-.2 1.1.4 2.3.6 3.6.6.6 0 1 .4 1 1V20c0 .6-.4 1-1 1A17 17 0 0 1 3 4c0-.6.4-1 1-1h3.5c.6 0 1 .4 1 1 0 1.3.2 2.5.6 3.6.1.3 0 .7-.2 1z"/></svg>
        +1 (808) 555 0172
      </li>
      <li>
        <svg viewBox="0 0 24 24" aria-hidden="true"><path d="M12 2a10 10 0 1 0 0 20 10 10 0 0 0 0-20zm6.9 6h-2.9a15.6 15.6 0 0 0-1.4-3.6A8 8 0 0 1 18.9 8zM12 4c.8 1.2 1.5 2.5 1.9 4h-3.8c.4-1.5 1.1-2.8 1.9-4zM4.3 14a8 8 0 0 1 0-4h3.4a16 16 0 0 0 0 4zm.8 2h2.9c.3 1.3.8 2.5 1.4 3.6A8 8 0 0 1 5.1 16zM8 8H5.1a8 8 0 0 1 4.3-3.6C8.8 5.5 8.3 6.7 8 8zm4 12c-.8-1.2-1.5-2.5-1.9-4h3.8c-.4 1.5-1.1 2.8-1.9 4zm2.3-6H9.7a14.6 14.6 0 0 1 0-4h4.6a14.6 14.6 0 0 1 0 4zm.3 5.6c.6-1.1 1.1-2.3 1.4-3.6h2.9a8 8 0 0 1-4.3 3.6zm1.7-5.6a16 16 0 0 0 0-4h3.4a8 8 0 0 1 0 4z"/></svg>
        www.purrlanenestco.example
      </li>
      <li>
        <svg viewBox="0 0 24 24" aria-hidden="true"><path d="M2 5h20v14H2zm2 2v.5l8 5 8-5V7zm0 2.8V17h16V9.8l-8 5z"/></svg>
        support@purrlanenestco.example
      </li>
    </ul>

    <span class="front__accent" aria-hidden="true"></span>
    <span class="front__band" aria-hidden="true"></span>
  </section>

  <section class="card card--back" aria-label="Business card back">
    <div class="back__photo" role="img" aria-label="Photograph of a fluffy orange and white cat resting in green grass"></div>
    <p class="back__brand">Purrlane Nest Co</p>
  </section>

</body>
</html>
```